Pyschiatry Experts need Marketing Campaign

Ad(s) developed for print advertising sharing our purpose and services, highlighting our medical care providers. Must be welcoming and inviting while displaying a high level of professionalism expected from a physician's office.

Target Market(s)

Local community

Industry/Entity Type

Psychiatry (Healthcare)

Requirements
Must have
• Staff pictures, 'Medication Management Experts', 'Prompt Appointments', 'ADD/ADHD, Bipolar Disorder, Depression, Anxiety, Schizophrenia, Grief Reaction and others' 'Virtual and In-Person Visits'
Nice to have
• Address: 412 E Marlowe Coeur d'Alene Phone (208)555-7813 website: BrightKestrel.example Hours: Mon - Thur 7am - 6pm

```html
<!DOCTYPE html>
<html lang="en">
<head>
<meta charset="utf-8">
<title>Medication Management Experts – Flyer</title>
<link href="https://fonts.googleapis.com/css2?family=Roboto+Condensed:wght@400;700&family=Fira+Sans:wght@400;500&family=Arimo:wght@400;700&display=swap" rel="stylesheet">
<style>
  :root{
    --stage:#bdbdbd;
  }
  *{box-sizing:border-box;margin:0;padding:0}
  html,body{width:1200px;height:866px;overflow:hidden;background:var(--stage)}
  .stage{position:relative;width:1200px;height:866px}

  .flyer{
    --hero:#b8dc5a; --band:#243b22; --panel:#f0ede0; --ink:#1f2a1c; --accent:#8db52a;
    --brand:#3fa3a0; --footer:#243b22; --footer-accent:#a9cf3f;
    --ic1:#7a6fd4; --ic2:#4a80e0; --ic3:#8a5a14; --ic4:#243b22;
    --photo-a:#e9d7b4; --photo-b:#c9a23a; --staff-a:#7d8590; --staff-b:#2a2e33;
    position:absolute; top:64px; width:524px; height:740px; background:#fff;
    font-family:"Arimo",Arial,sans-serif; color:var(--ink); overflow:hidden;
  }
  .flyer--color{left:65px}
  .flyer--mono{
    left:613px;
    --hero:#d3d3d3; --band:#464646; --panel:#efefef; --ink:#2a2a2a; --accent:#9a9a9a;
    --brand:#9a9a9a; --footer:#464646; --footer-accent:#bdbdbd;
    --ic1:#8a8a8a; --ic2:#9a9a9a; --ic3:#8c8c8c; --ic4:#3c3c3c;
    --photo-a:#e2e2e2; --photo-b:#9a9a9a; --staff-a:#9a9a9a; --staff-b:#2e2e2e;
  }

  .hero-block{position:absolute;left:0;top:0;width:295px;height:160px;background:var(--hero)}
  .headline{position:absolute;left:45px;top:40px;font-family:"Roboto Condensed",sans-serif;font-weight:700;
    font-size:36px;line-height:37px;color:var(--ink);letter-spacing:.2px}
  .intro-band{position:absolute;left:0;top:160px;width:295px;height:63px;background:var(--band)}
  .intro-band p{position:absolute;left:45px;top:6px;font-family:"Fira Sans",sans-serif;font-size:21px;line-height:24px;color:#fff}
  .hero-photo{position:absolute;left:295px;top:0;width:229px;height:223px;
    background:radial-gradient(circle at 68% 32%, var(--photo-b) 0 22%, transparent 48%),linear-gradient(160deg,var(--photo-a),#d8d4cc 70%,#b9b4aa)}

  .providers{position:absolute;left:0;top:223px;width:524px;height:303px;background:var(--panel)}
  .provider{position:absolute;top:4px;width:106px}
  .provider:nth-child(1){left:33px}.provider:nth-child(2){left:151px}.provider:nth-child(3){left:268px}.provider:nth-child(4){left:384px}
  .provider__photo{height:123px;background:radial-gradient(ellipse at 50% 40%,var(--staff-a),var(--staff-b) 80%)}
  .provider__name{height:28px;background:var(--hero);text-align:center;font-size:10px;line-height:11.5px;padding-top:3px}
  .provider__name b{display:block;font-weight:700}
  .provider__bio{margin-top:7px;text-align:center;font-size:7.6px;line-height:9.5px;color:#222}

  .services{position:absolute;left:33px;top:544px;width:310px;font-size:9.6px;line-height:11.6px}
  .services strong{font-weight:700}
  .portal{position:absolute;left:33px;top:619px;font-family:"Roboto Condensed",sans-serif;font-size:11px;color:var(--accent)}
  .features{position:absolute;left:30px;top:628px;width:310px;height:50px;display:flex}
  .feature{position:relative;text-align:center;font-size:8.6px;padding-top:30px}
  .feature + .feature{border-left:1px solid #ddd}
  .feature svg{position:absolute;top:3px;left:50%;margin-left:-13px}
  .feature:nth-child(1){width:80px}.feature:nth-child(2){width:101px}.feature:nth-child(3){width:71px}.feature:nth-child(4){width:58px}
  .hours{position:absolute;left:31px;top:673px;font-family:"Roboto Condensed",sans-serif;font-size:16px;color:#333}
  .hours span{color:var(--accent)}

  .divider{position:absolute;left:357px;top:540px;width:1px;height:150px;background:#ddd}
  .contact{position:absolute;left:362px;top:548px;width:158px;text-align:center;font-size:8.6px;line-height:10.5px;color:#333}
  .brand{display:flex;flex-direction:column;align-items:center;gap:6px;margin-bottom:10px}
  .brand__dot{width:30px;height:30px;border-radius:50%;background:var(--brand)}
  .brand__name{font-family:"Arimo",Arial,sans-serif;font-size:13px;font-weight:400;color:var(--brand);letter-spacing:.5px;line-height:15px}
  .contact h3{font-family:"Roboto Condensed",sans-serif;font-weight:700;font-size:8.6px;color:var(--accent);margin-bottom:12px}
  .contact p{margin-bottom:5px}
  .contact .lbl{font-family:"Roboto Condensed",sans-serif;font-weight:700;color:var(--accent)}

  .tagline{position:absolute;left:0;bottom:0;width:524px;height:37px;background:var(--footer);
    text-align:center;font-family:"Roboto Condensed",sans-serif;font-size:19px;line-height:37px;color:#fff}
  .tagline span{color:var(--footer-accent)}
</style>
</head>
<body>
<div class="stage">

  <!-- colour version -->
  <section class="flyer flyer--color">
    <div class="hero-block"><h1 class="headline">MEDICATION<br>MANAGEMENT<br>EXPERTS</h1></div>
    <div class="intro-band"><p>Meet Our<br>Mental Health Providers</p></div>
    <div class="hero-photo" role="img" aria-label="Photo of a smiling woman in a yellow top using her phone on a sofa"></div>

    <div class="providers">
      <article class="provider">
        <div class="provider__photo" role="img" aria-label="Portrait of Dan Mercer"></div>
        <div class="provider__name"><b>Dan Mercer,</b>PMHNP - BC</div>
        <p class="provider__bio">Before entering into healthcare, Daniel spent years in academia researching foundational cellular and molecular biology mechanisms along with genetics that has provided a strong basis for understanding complex psychiatric conditions and the medications used in behavioral health. Dan cares for teenagers thru adult patients populations.</p>
      </article>
      <article class="provider">
        <div class="provider__photo" role="img" aria-label="Portrait of Warren Pike"></div>
        <div class="provider__name"><b>Warren Pike,</b>PMHNP - BC</div>
        <p class="provider__bio">With a former career in the inpatient behavioral health environment, Warren is excited to share her experience and passion for mental health in an outpatient setting. Her practice cares for teenagers to adults in all aspects of psychiatry and mental wellness.</p>
      </article>
      <article class="provider">
        <div class="provider__photo" role="img" aria-label="Portrait of Rae Lindell"></div>
        <div class="provider__name"><b>Rae Lindell</b>PMHNP - BC</div>
        <p class="provider__bio">Formally from North Idaho and having moved back to this area, Rae brings several years of pediatric and adolescent experience to Bright Kestrel Health. Outside of work, Rae enjoys spending time with his wife and two children, exploring various outdoor pursuits including backpacking, fishing, and all things Bigfoot.</p>
      </article>
      <article class="provider">
        <div class="provider__photo" role="img" aria-label="Portrait of Joan Ashby"></div>
        <div class="provider__name"><b>Joan Ashby,</b>PMHNP-BC, DNP</div>
        <p class="provider__bio">Dr. Joan Ashby is Board Certified in Geriatric and Adult Psychiatric Medicine. She has practiced Psychiatry for over 30 years and has extensive experience in the diagnosis and treatment of major mental illnesses. Her passion for mental wellness values the long term relationship with the adult and geriatric patient.</p>
      </article>
    </div>

    <p class="services"><strong>Bringing comprehensive evaluation, medication management and psychotherapy to the full spectrum of mental health disorders including:</strong><br>Minor, moderate and major depression, bipolar disorder, ADD/ADHD, anxiety, schizophrenia, stress or grief reactions, and others.</p>
    <p class="portal">We know your days are busy! &nbsp;Use our Patient Portal for:</p>
    <div class="features">
      <div class="feature"><svg width="26" height="26"><circle cx="13" cy="13" r="13" fill="var(--ic1)"/><circle cx="13" cy="13" r="4.5" fill="none" stroke="#fff" stroke-width="1"/></svg>Online Massaging</div>
      <div class="feature"><svg width="26" height="26"><circle cx="13" cy="13" r="13" fill="var(--ic2)"/><path d="M10 17l1-3 5-5 2 2-5 5z" fill="none" stroke="#fff" stroke-width="1"/></svg>Prescription Renewal</div>
      <div class="feature"><svg width="26" height="26"><circle cx="13" cy="13" r="13" fill="var(--ic3)"/><rect x="8" y="10" width="7" height="6" fill="none" stroke="#fff" stroke-width="1"/><path d="M15 12l4-2v6l-4-2" fill="none" stroke="#fff" stroke-width="1"/></svg>Virtual Visits</div>
      <div class="feature"><svg width="26" height="26"><circle cx="13" cy="13" r="13" fill="var(--ic4)"/><rect x="8" y="10" width="10" height="6" fill="none" stroke="#fff" stroke-width="1"/><circle cx="13" cy="13" r="1.5" fill="none" stroke="#fff" stroke-width="1"/></svg>Pay Your Bill</div>
    </div>
    <p class="hours"><span>Hours:</span> Mon - Thur 7am - 6pm</p>

    <div class="divider"></div>
    <div class="contact">
      <div class="brand"><div class="brand__dot"></div><div class="brand__name">BRIGHT KESTREL<br>HEALTH</div></div>
      <h3>Contact us:</h3>
      <p>Bright Kestrel Health<br>412 E Marlowe Coeur d'Alene</p>
      <p><span class="lbl">Phone:</span> (208)555-7813</p>
      <p><span class="lbl">Website:</span> BrightKestrel.example</p>
    </div>

    <div class="tagline"><span>WE CARE</span> FOR YOUR HEALTH</div>
  </section>

  <!-- greyscale version -->
  <section class="flyer flyer--mono">
    <div class="hero-block"><h1 class="headline">MEDICATION<br>MANAGEMENT<br>EXPERTS</h1></div>
    <div class="intro-band"><p>Meet Our<br>Mental Health Providers</p></div>
    <div class="hero-photo" role="img" aria-label="Greyscale photo of a smiling woman using her phone on a sofa"></div>

    <div class="providers">
      <article class="provider">
        <div class="provider__photo" role="img" aria-label="Portrait of Dan Mercer"></div>
        <div class="provider__name"><b>Dan Mercer,</b>PMHNP - BC</div>
        <p class="provider__bio">Before entering into healthcare, Daniel spent years in academia researching foundational cellular and molecular biology mechanisms along with genetics that has provided a strong basis for understanding complex psychiatric conditions and the medications used in behavioral health. Dan cares for teenagers thru adult patients populations.</p>
      </article>
      <article class="provider">
        <div class="provider__photo" role="img" aria-label="Portrait of Warren Pike"></div>
        <div class="provider__name"><b>Warren Pike,</b>PMHNP - BC</div>
        <p class="provider__bio">With a former career in the inpatient behavioral health environment, Warren is excited to share her experience and passion for mental health in an outpatient setting. Her practice cares for teenagers to adults in all aspects of psychiatry and mental wellness.</p>
      </article>
      <article class="provider">
        <div class="provider__photo" role="img" aria-label="Portrait of Rae Lindell"></div>
        <div class="provider__name"><b>Rae Lindell</b>PMHNP - BC</div>
        <p class="provider__bio">Formally from North Idaho and having moved back to this area, Rae brings several years of pediatric and adolescent experience to Bright Kestrel Health. Outside of work, Rae enjoys spending time with his wife and two children, exploring various outdoor pursuits including backpacking, fishing, and all things Bigfoot.</p>
      </article>
      <article class="provider">
        <div class="provider__photo" role="img" aria-label="Portrait of Joan Ashby"></div>
        <div class="provider__name"><b>Joan Ashby,</b>PMHNP-BC, DNP</div>
        <p class="provider__bio">Dr. Joan Ashby is Board Certified in Geriatric and Adult Psychiatric Medicine. She has practiced Psychiatry for over 30 years and has extensive experience in the diagnosis and treatment of major mental illnesses. Her passion for mental wellness values the long term relationship with the adult and geriatric patient.</p>
      </article>
    </div>

    <p class="services"><strong>Bringing comprehensive evaluation, medication management and psychotherapy to the full spectrum of mental health disorders including:</strong><br>Minor, moderate and major depression, bipolar disorder, ADD/ADHD, anxiety, schizophrenia, stress or grief reactions, and others.</p>
    <p class="portal">We know your days are busy! &nbsp;Use our Patient Portal for:</p>
    <div class="features">
      <div class="feature"><svg width="26" height="26"><circle cx="13" cy="13" r="13" fill="var(--ic1)"/><circle cx="13" cy="13" r="4.5" fill="none" stroke="#fff" stroke-width="1"/></svg>Online Massaging</div>
      <div class="feature"><svg width="26" height="26"><circle cx="13" cy="13" r="13" fill="var(--ic2)"/><path d="M10 17l1-3 5-5 2 2-5 5z" fill="none" stroke="#fff" stroke-width="1"/></svg>Prescription Renewal</div>
      <div class="feature"><svg width="26" height="26"><circle cx="13" cy="13" r="13" fill="var(--ic3)"/><rect x="8" y="10" width="7" height="6" fill="none" stroke="#fff" stroke-width="1"/><path d="M15 12l4-2v6l-4-2" fill="none" stroke="#fff" stroke-width="1"/></svg>Virtual Visits</div>
      <div class="feature"><svg width="26" height="26"><circle cx="13" cy="13" r="13" fill="var(--ic4)"/><rect x="8" y="10" width="10" height="6" fill="none" stroke="#fff" stroke-width="1"/><circle cx="13" cy="13" r="1.5" fill="none" stroke="#fff" stroke-width="1"/></svg>Pay Your Bill</div>
    </div>
    <p class="hours"><span>Hours:</span> Mon - Thur 7am - 6pm</p>

    <div class="divider"></div>
    <div class="contact">
      <div class="brand"><div class="brand__dot"></div><div class="brand__name">BRIGHT KESTREL<br>HEALTH</div></div>
      <h3>Contact us:</h3>
      <p>Bright Kestrel Health<br>412 E Marlowe Coeur d'Alene</p>
      <p><span class="lbl">Phone:</span> (208)555-7813</p>
      <p><span class="lbl">Website:</span> BrightKestrel.example</p>
    </div>

    <div class="tagline"><span>WE CARE</span> FOR YOUR HEALTH</div>
  </section>

</div>
</body>
</html>
```